Wed site for biomedical device startup

We need a generic website for a medical device startup. I will provide examples below of websites from other companies that can serve as models for what we are looking for. The startup is for a device that can non invasively measure blood flow in the brain using light. The application is to detect the type of stroke someone is having before they get to the hospital so treatment can be started right away. This saves patients upto hours of delayed treatment. Patients will be able to recover from stroke much better and faster as a result. I have attached an AI generated illustration of what the device will ultimately look like for reference.

https://www.872vantora.com
https://quilvesta.com

Target Market(s)

Biomedical, medical device, investors of biomedical device startups

Industry/Entity Type

Biomedical

Coding

Coded - Design and coding required

Number of Pages Required

4 page

Requirements
Must have
• same section and section headings as example websites listed above
Nice to have
• similar to example websites listed above. Prefer a darker website over a lighter one. Perhaps dark blues to go with logo colors. A moving background image element at top of landing page could be cool. Something indicative of heartbeat, or neurons, or blood flow.

```html
<!DOCTYPE html>
<html lang="en">
<head>
<meta charset="utf-8">
<title>LUMVEX — Pioneering Tomorrow's Healthcare</title>
<link href="https://fonts.googleapis.com/css2?family=Michroma&family=Lato:wght@400;700&display=swap" rel="stylesheet">
<style>
:root{
  --navy:#0c0a3a;
  --navy-deep:#05041f;
  --ink:#ffffff;
  --muted:#cfd3f2;
  --cyan:#22c4e3;
  --violet:#7a1fd6;
  --purple:#4b1a9e;
  --blue:#1f3fbf;
}
*{margin:0;padding:0;box-sizing:border-box}
html,body{width:1200px;height:5038px;overflow:hidden;background:var(--navy);color:var(--ink);font-family:'Lato',sans-serif}
.page{position:relative;width:1200px;height:5038px}
section,header,footer{position:absolute;left:0;width:1200px;overflow:hidden}
.abs{position:absolute}
h1,h2,h3,.nav a,.btn,.brand{font-family:'Michroma',sans-serif;font-weight:400;text-transform:uppercase}
h2{font-size:25px;line-height:41px;letter-spacing:1px}
p{font-size:14.5px;line-height:25.5px;color:var(--ink)}
.btn{position:absolute;display:flex;align-items:center;justify-content:center;font-size:14px;border-radius:5px;text-decoration:none}
.btn-light{background:#fff;color:#141440}
.btn-grad{background:linear-gradient(90deg,var(--violet),var(--cyan));color:#fff}

/* header + hero */
.hero{top:0;height:651px;background:
  radial-gradient(ellipse 50% 35% at 50% 45%,rgba(70,120,230,.55),transparent 70%),
  radial-gradient(ellipse 40% 40% at 15% 90%,rgba(140,40,220,.6),transparent 70%),
  radial-gradient(ellipse 35% 40% at 90% 85%,rgba(120,40,210,.5),transparent 70%),
  linear-gradient(180deg,#14104d,#1d1a6e 50%,#2a168a)}
.brand{display:flex;align-items:center;gap:14px;font-size:40px;letter-spacing:1px;color:#fff}
.brand .dot{width:62px;height:62px;border-radius:50%;background:linear-gradient(135deg,var(--cyan),var(--violet))}
.nav{position:absolute;top:42px;left:0;width:1200px;height:20px}
.nav a{position:absolute;font-size:14px;color:#fff;text-decoration:none}
.nav a.active{color:var(--cyan)}
.hero h1{position:absolute;top:222px;left:0;width:1212px;text-align:center;font-size:47px;line-height:62px;letter-spacing:1px}
.hero p{position:absolute;top:370px;left:250px;width:712px;text-align:center;font-size:15px;line-height:29px}

/* innovation */
.innovation{top:651px;height:424px;background:linear-gradient(90deg,#03031a 0%,#05062a 45%,#0a2a7a 70%,#1d5fd0 100%)}
.innovation .art{position:absolute;left:645px;top:0;width:555px;height:424px;background:radial-gradient(ellipse 45% 55% at 35% 55%,rgba(60,160,255,.75),transparent 75%),radial-gradient(ellipse 40% 40% at 80% 30%,rgba(60,130,230,.5),transparent 70%)}

/* blood loss */
.monitoring{top:1075px;height:926px;background:
  radial-gradient(ellipse 30% 25% at 0% 10%,rgba(140,30,220,.85),transparent 70%),
  radial-gradient(ellipse 30% 25% at 80% 92%,rgba(30,150,220,.55),transparent 70%),
  var(--navy-deep)}
.feature{position:absolute;left:111px;width:450px}
.feature .ico{position:absolute;left:0;top:2px;width:34px;height:34px;border-radius:50%;background:linear-gradient(135deg,var(--violet),var(--cyan));display:flex;align-items:center;justify-content:center}
.feature h3{font-family:'Lato',sans-serif;font-weight:700;text-transform:none;font-size:16px;margin-left:50px;line-height:22px}
.feature p{margin-left:52px;font-size:13.5px;line-height:26px}
.photo-frame{position:absolute;left:612px;top:113px;width:476px;height:692px;border-radius:12px;padding:3px;background:linear-gradient(160deg,var(--violet),var(--cyan))}
.photo-frame .fill{width:100%;height:100%;border-radius:10px;background:linear-gradient(160deg,#d8d6d8,#b7957f 45%,#8b6a58 70%,#e7e5e6)}

/* how we help */
.help{top:2001px;height:574px;background:linear-gradient(95deg,#3a1a9a 0%,#5b2bd0 30%,#3d6fe0 65%,#22c4e3 100%)}
.help .waves{position:absolute;left:0;top:0;width:560px;height:574px;background:radial-gradient(ellipse 60% 45% at 30% 50%,rgba(180,160,255,.35),transparent 70%),radial-gradient(ellipse 40% 30% at 50% 90%,rgba(160,40,220,.6),transparent 70%)}

/* life changing */
.life{top:2575px;height:673px;background:radial-gradient(ellipse 30% 30% at 10% 8%,rgba(30,190,230,.7),transparent 70%),#0a0930}
.life .art{position:absolute;left:600px;top:0;width:600px;height:673px;background:linear-gradient(180deg,#e8d9c4 0%,#d3b99a 35%,#c98a4a 62%,#e89a3a 72%,#4a3a2a 85%,#2a2220 100%)}
.life ul{list-style:none;position:absolute;left:111px;top:2917px;}
.bullets li{position:absolute;left:111px;font-size:14.5px}

/* nirds */
.nirds{top:3248px;height:670px;background:radial-gradient(ellipse 30% 30% at 95% 10%,rgba(150,40,230,.75),transparent 70%),#0c0a3a}
.nirds .art{position:absolute;left:0;top:0;width:600px;height:670px;background:radial-gradient(ellipse 30% 50% at 42% 55%,rgba(60,170,255,.65),transparent 75%),linear-gradient(180deg,#05103a,#0a1d5a)}

/* team */
.team{top:3918px;height:645px;background:
  radial-gradient(ellipse 25% 25% at 5% 10%,rgba(30,190,230,.6),transparent 70%),
  radial-gradient(ellipse 25% 30% at 95% 80%,rgba(150,40,230,.7),transparent 70%),
  radial-gradient(ellipse 60% 20% at 50% 45%,rgba(80,90,220,.45),transparent 70%),
  #17145a}
.team h2{position:absolute;top:109px;left:0;width:1200px;text-align:center;font-size:25px}
.member{position:absolute;top:194px;width:300px;text-align:center}
.member .portrait{width:246px;height:246px;margin:0 auto;border-radius:50%;background:linear-gradient(160deg,#8a9a80,#5b4a3e 60%,#2c2a2a)}
.member h3{margin-top:28px;font-size:20px}
.member p{font-size:14.5px;line-height:22px}

/* footer */
.site-footer{top:4563px;height:475px;background:radial-gradient(ellipse 35% 40% at 100% 95%,rgba(130,30,210,.55),transparent 70%),#100d45}
.fcol{position:absolute;top:91px}
.fcol h4{font-family:'Michroma',sans-serif;font-weight:400;font-size:15px;text-transform:uppercase;margin-bottom:12px}
.fcol a,.fcol span{display:block;font-size:15px;line-height:41px;color:var(--muted);text-decoration:none}
.copy{position:absolute;left:444px;top:412px;font-size:14.5px}
</style>
</head>
<body>
<div class="page">

<header class="hero">
  <div class="brand abs" style="left:111px;top:16px">
    <span class="dot"></span>LUMVEX
  </div>
  <nav class="nav">
    <a class="active" style="left:483px">Home</a>
    <a style="left:600px">About</a>
    <a style="left:725px">Technology</a>
    <a style="left:913px">Press</a>
    <a style="left:1036px">Contact</a>
  </nav>
  <h1>Pioneering Tomorrow’s<br>Healthcare</h1>
  <p>We develop next-generation biomedical technologies to transform patient care and elevate human health outcomes.</p>
  <a class="btn btn-light" style="left:479px;top:447px;width:242px;height:53px">Connect with us</a>
</header>

<section class="innovation">
  <div class="art" role="img" aria-label="Glowing blue anatomical heart with a heartbeat line"></div>
  <h2 class="abs" style="left:111px;top:101px;width:520px">Where innovation meets biology</h2>
  <p class="abs" style="left:111px;top:194px;width:500px">Accelerating the future of medicine through cutting-edge research, precision engineering, and life-saving innovation.</p>
  <a class="btn btn-light" style="left:111px;top:273px;width:329px;height:53px">Explore our technology</a>
</section>

<section class="monitoring">
  <h2 class="abs" style="left:111px;top:189px;width:470px">Innovative blood loss monitoring</h2>
  <div class="feature" style="top:299px">
    <span class="ico"><svg width="16" height="16" viewBox="0 0 16 16"><rect x="2" y="3" width="12" height="8" rx="1" fill="none" stroke="#fff" stroke-width="1.6"/><path d="M1 13h14" stroke="#fff" stroke-width="1.6"/></svg></span>
    <h3>Portable Monitoring</h3>
    <p>Lorem ipsum dolor sit amet, consectetur adipiscing elit, sed do eiusmod tempor ine et dolore magna aliqua.</p>
  </div>
  <div class="feature" style="top:415px">
    <span class="ico"><svg width="16" height="16" viewBox="0 0 16 16"><circle cx="8" cy="8" r="5.5" fill="none" stroke="#fff" stroke-width="1.6"/><circle cx="8" cy="8" r="2" fill="#fff"/></svg></span>
    <h3>Real-time Alerts</h3>
    <p>Duis aute irure dolor in reprehenderit in voluptate velit esse cillum dolore eu fugiat nulla pariatur.</p>
  </div>
  <div class="feature" style="top:542px">
    <span class="ico"><svg width="16" height="16" viewBox="0 0 16 16"><circle cx="8" cy="4.5" r="2.5" fill="#fff"/><path d="M3 14c0-3 2-5 5-5s5 2 5 5z" fill="#fff"/></svg></span>
    <h3>Patient-Centered</h3>
    <p>Aute irure dolor in reprehenderit in voluptate velit esse cillum dolore eu fugiat nulla pariatur.</p>
  </div>
  <a class="btn btn-grad" style="left:111px;top:660px;width:178px;height:55px">Learn more</a>
  <div class="photo-frame"><div class="fill" role="img" aria-label="Photo of a patient wearing a light-based brain monitoring headband"></div></div>
</section>

<section class="help">
  <div class="waves" role="img" aria-label="Flowing wave line background"></div>
  <h2 class="abs" style="left:596px;top:99px">How we help</h2>
  <p class="abs" style="left:596px;top:145px;width:480px;font-size:14px">Lorem ipsum dolor sit amet, consectetur adipiscing elit, sed do eiusmod tempor incididunt ut labore et dolore magna aliqua. Ut enim ad minim veniam, quis nostrud exercitation ullamco laboris nisi ut aliquip ex ea commodo consequat.</p>
  <p class="abs" style="left:596px;top:274px;width:480px;font-size:14px">Duis aute irure dolor in reprehenderit in voluptate velit esse cillu m dolore eu fugiat nulla pariatur. Excepteur sint occaecat cupi datat non proident, sunt in culpa qui officia deserunt mollit anim id est laborum.</p>
  <a class="btn btn-light" style="left:598px;top:379px;width:186px;height:55px">Learn more</a>
</section>

<section class="life">
  <div class="art" role="img" aria-label="Hand holding a glowing brain against a sunset sky"></div>
  <h2 class="abs" style="left:111px;top:154px;width:420px">Life-changing technology for adults infants</h2>
  <p class="abs" style="left:111px;top:295px;font-size:14px;font-weight:700">WHAT IS IT NIRDS</p>
  <p class="abs" style="left:111px;top:340px">• Quis autem vel eum iure reprehenderit qui in ea voluptate</p>
  <p class="abs" style="left:111px;top:381px">• Excepteur sint occaecat cupidatat</p>
  <p class="abs" style="left:111px;top:422px">• Duis aute irure dolor in reprehenderit</p>
  <a class="btn btn-grad" style="left:111px;top:477px;width:178px;height:53px">Read more</a>
</section>

<section class="nirds">
  <div class="art" role="img" aria-label="Glowing digital human figure surrounded by medical icons"></div>
  <h2 class="abs" style="left:719px;top:138px">NIRDS explained</h2>
  <p class="abs" style="left:719px;top:186px;width:380px;font-size:14px">Lorem ipsum dolor sit amet, consectetur adipiscing elit, sed do eiusmod tempor incididunt ut labore et dolore magna aliqua. Ut enim ad minim veniam, quis nostrud exercitation ullamco laboris nisi ut aliquip ex ea commodo consequat.</p>
  <p class="abs" style="left:719px;top:340px;width:380px;font-size:14px">Duis aute irure dolor in reprehenderit in voluptate velit esse cillu m dolore eu fugiat nulla pariatur. Excepteur sint occaecat cupi datat non proident, sunt in culpa qui officia deserunt mollit anim id est laborum.</p>
  <a class="btn btn-grad" style="left:719px;top:471px;width:180px;height:53px">Read more</a>
</section>

<section class="team">
  <h2>Our team</h2>
  <div class="member" style="left:124px">
    <div class="portrait" role="img" aria-label="Portrait photo of Maria"></div>
    <h3>Maria</h3><p>Excepteur sint occaecat</p>
  </div>
  <div class="member" style="left:450px">
    <div class="portrait" role="img" aria-label="Portrait photo of Davise"></div>
    <h3>Davise</h3><p>Duis aute irure dolor</p>
  </div>
  <div class="member" style="left:774px">
    <div class="portrait" role="img" aria-label="Portrait photo of John Doe"></div>
    <h3>John Doe</h3><p>Duis aute irure dolor</p>
  </div>
</section>

<footer class="site-footer">
  <div class="brand abs" style="left:111px;top:103px">
    <span class="dot"></span>LUMVEX
  </div>
  <div class="fcol" style="left:444px">
    <h4>Quick links</h4>
    <a>Home</a><a>About</a><a>Technology</a><a>Press</a><a>Contact Us</a>
  </div>
  <div class="fcol" style="left:674px">
    <h4>Help links</h4>
    <a>FAQ</a><a>Term of Use</a><a>Privacy Policy</a><a>Support Links</a><a>Terms &amp; Conditions</a>
  </div>
  <div class="fcol" style="left:918px">
    <h4>Contact us</h4>
    <span>LUMVEX, United States</span><span>+1 888 888 8888</span><span>info@lumvex.com</span>
  </div>
  <p class="copy">Copyrights@2025.LUMVEX.All Rights Reserved</p>
</footer>

</div>
</body>
</html>
```